Business card design needed

Hi,
I was hoping to have a business card designed with a background similar to dark coloured concrete texture. I have a photo of the particular concrete that I would like to be used as the background but for some reason it wouldn't let me upload the image. Please email me for the image and I will send to you asap.
I would like the company name to be in a font that is thin, crisp to reflect 'precision'. I am trying to convey that my services are more precise and have more attention to detail than my competitors. I would like this to be represented through the font if possible.
Colours are at your discretion - although we would like it to attract the eye and stand out. We would like the card to be in a modern style.
I was thinking for an image in the background of the card, or on the side of the card wherever is appropriate, half of a ring saw blade or similar.
The company is a concrete cutting and drilling service - we are a 24 hour 7 day service which is unique to the industry. We provide a more detailed service to our customers and this is the backbone of our reputation.
Target Market(s)
Construction industry & general public
Industry/Entity Type
Concrete
Contact Information for Business Card
Ridgeline Saw & Bore Pty Ltd
Concrete Cutting & Drilling
24 hour 7 day service
Trevor Halloway
Director
M: 0412 908 251
P: (07) 3196 4027
E: ridgelinesawandbore@mailbrook.example
PO Box 318, Wendaroo DC QLD 4172

```html
<!DOCTYPE html>
<html lang="en">
<head>
<meta charset="utf-8">
<title>Ridgeline Saw &amp; Bore — Business Card</title>
<link rel="stylesheet" href="https://fonts.googleapis.com/css2?family=Inter:wght@200&family=Noto+Sans:wght@700&family=Open+Sans:wght@700;800&family=Source+Sans+3:wght@400;600&display=swap">
<style>
  :root {
    --ink: #000000;
    --orange: #f37021;
    --slate: #717174;
    --muted: #8a8a8c;
    --white: #ffffff;
  }
  html, body {
    margin: 0;
    padding: 0;
    width: 1200px;
    height: 693px;
    overflow: hidden;
    background: var(--white);
  }
  .card {
    position: relative;
    width: 1200px;
    height: 693px;
    background: var(--orange);
    overflow: hidden;
  }
  .identity-panel {
    position: absolute;
    left: 0;
    top: 0;
    width: 694px;
    height: 693px;
    background: var(--ink);
  }
  .wordmark, .company-name {
    position: absolute;
    left: 0;
    top: 0;
  }
  .wordmark text {
    font-family: "Inter", sans-serif;
    font-weight: 200;
    fill: var(--orange);
  }
  .company-name text {
    font-family: "Noto Sans", sans-serif;
    font-weight: 700;
    fill: var(--slate);
  }
  .tagline text {
    font-family: "Source Sans 3", sans-serif;
    font-weight: 400;
    fill: var(--orange);
  }
  .person {
    position: absolute;
    left: 0;
    width: 698px;
    top: 332px;
    text-align: center;
    font-family: "Open Sans", sans-serif;
  }
  .person-name {
    margin: 0;
    font-family: "Open Sans", sans-serif;
    font-weight: 700;
    font-size: 31px;
    line-height: 42px;
    color: var(--white);
  }
  .person-role {
    margin: 0;
    font-family: "Source Sans 3", sans-serif;
    font-weight: 400;
    font-size: 28px;
    line-height: 40px;
    color: var(--muted);
  }
  .contact {
    position: absolute;
    left: 0;
    width: 698px;
    top: 555px;
    margin: 0;
    text-align: center;
    font-family: "Source Sans 3", sans-serif;
    font-style: normal;
    font-size: 25px;
    line-height: 34px;
    color: var(--muted);
  }
  .contact span { display: block; }
  .photo-frame {
    position: absolute;
    left: 0;
    top: 0;
  }
  .photo-label {
    font-family: "Open Sans", sans-serif;
    font-weight: 800;
    fill: var(--white);
  }
</style>
</head>
<body>
<main class="card">
  <svg class="photo-frame" width="1200" height="693" viewBox="0 0 1200 693">
    <path class="photo-frame-shadow" d="M694 51 H1098 A56 56 0 0 1 1154 107 V620 A26 26 0 0 1 1128 646 H694 Z" fill="var(--ink)"/>
    <g role="img" aria-label="Photograph of a concrete-cutting ring saw blade">
      <path class="photo-well" d="M694 64 H1088 A50 50 0 0 1 1138 114 V608 A22 22 0 0 1 1116 630 H694 Z" fill="var(--slate)"/>
      <text class="photo-label" x="914" y="385" font-size="107" text-anchor="middle" transform="rotate(-30 914 350)">IMAGE</text>
    </g>
  </svg>

  <section class="identity-panel">
    <svg class="wordmark" width="694" height="160" viewBox="0 0 694 160">
      <text x="46" y="141" font-size="122" textLength="605" lengthAdjust="spacingAndGlyphs">RIDGELINE</text>
    </svg>
    <svg class="company-name" width="694" height="260" viewBox="0 0 694 260">
      <text x="47" y="198" font-size="36" textLength="605" lengthAdjust="spacingAndGlyphs">RIDGELINE SAW &amp; BORE PTY LTD</text>
      <g class="tagline">
        <text x="47" y="236" font-size="25" textLength="603" lengthAdjust="spacingAndGlyphs">Concrete Cutting &amp; Drilling  |  24 hours 7 day service</text>
      </g>
    </svg>

    <div class="person">
      <p class="person-name">Trevor Halloway</p>
      <p class="person-role">Director</p>
    </div>

    <address class="contact">
      <span>PO Box 318, Wendaroo DC QLD 4172</span>
      <span>M: 0412 908 251 P: (07) 3196 4027</span>
      <span>E: ridgelinesawandbore@mailbrook.example</span>
    </address>
  </section>
</main>
</body>
</html>
```